Pagecraft 6 pages GLAM design for hair salon

Hi guys.
I need a glam & easy to navigate web design for my (women only) new hair salon.
I have a logo. You can see in attached files.
I like 3d backgrounds.
My favourite colours choice: any variety of pink(hot & very soft), white, black, grey.
I would like to see website very feminine, glamorous & kind of old Hollywood and Dorinda Kessaly inspired.
Of course it should have plug ins, like social media, map, security etc.
My website now: http://velmorinstyling.example

Designs what I like:
http://trulanbeauty.example
http://pevrilglowlounge.example
http://www.quintarvisualworks.example/boutique-graphic-web-folio.html

Target Market(s)

WOMEN

Industry/Entity Type

Boutique

Requirements
Should not have
• any cartoon or other characters!

```html
<!DOCTYPE html>
<html lang="en">
<head>
<meta charset="utf-8">
<title>VELMORIN Hair Studio</title>
<link rel="stylesheet" href="https://fonts.googleapis.com/css2?family=Squada+One&family=Open+Sans:wght@400;700&display=swap">
<style>
  :root {
    --stripe-light: #f9c6d2;
    --stripe-dark: #f3b0c1;
    --frame-pink: #f7b9c8;
    --hot-pink: #ef3d8f;
    --soft-pink: #fbc4cf;
    --teal: #0f5c68;
    --sky: #7fd3e2;
    --ink: #111111;
    --band: #141414;
    --grey-light: #e2e2e2;
    --grey-mid: #c9c9c9;
    --text-dark: #333333;
    --white: #ffffff;
  }
  * { margin: 0; padding: 0; box-sizing: border-box; }
  html, body { width: 1200px; height: 675px; overflow: hidden; }
  body {
    position: relative;
    font-family: "Open Sans", Arial, sans-serif;
    background: repeating-linear-gradient(90deg, var(--stripe-light) 0 44px, var(--stripe-dark) 44px 88px);
  }
  .main-nav a {
    position: absolute;
    top: 28px;
    font-family: "Squada One", Impact, sans-serif;
    font-size: 21px;
    font-variant: small-caps;
    color: var(--ink);
    text-decoration: none;
    letter-spacing: 0.5px;
  }
  .main-nav .is-active {
    border-top: 1px solid var(--ink);
    border-bottom: 1px solid var(--ink);
    padding: 4px 9px 8px;
    top: 22px;
  }
  .page-frame {
    position: absolute;
    left: 101px; top: 70px;
    width: 984px; height: 620px;
    background: var(--frame-pink);
    box-shadow: 0 0 12px rgba(120, 40, 70, 0.3);
  }
  .logo {
    position: absolute;
    left: 494px; top: -27px;
    width: 176px; height: 176px;
    border-radius: 50%;
    background: var(--ink);
    border: 6px solid var(--frame-pink);
    display: flex; flex-direction: column; align-items: center; justify-content: center;
    z-index: 5;
    color: var(--white);
    font-family: "Open Sans", Arial, sans-serif;
    font-weight: 700;
    text-align: center;
    line-height: 1.1;
  }
  .logo .logo-name { font-size: 25px; letter-spacing: 0.5px; }
  .logo .logo-sub { font-size: 14px; }
  .hero {
    position: absolute;
    left: 110px; top: 79px;
    width: 966px; height: 351px;
    background: linear-gradient(90deg, #6cc9dc 0%, var(--sky) 50%, #6cc9dc 100%);
    overflow: hidden;
  }
  .hero-headline {
    position: absolute;
    left: 0; right: 0; top: 166px;
    text-align: center;
    font-family: "Squada One", Impact, sans-serif;
    text-transform: uppercase;
    font-size: 54px;
    line-height: 52px;
    color: var(--teal);
    letter-spacing: 2.5px;
    padding-left: 10px;
  }
  .hero-headline .initial { font-size: 58px; }
  .hero-arrow { position: absolute; top: 188px; }
  .hero-arrow.prev { left: 11px; }
  .hero-arrow.next { right: 11px; }
  .hero-dots { position: absolute; top: 332px; left: 459px; display: flex; gap: 8px; }
  .hero-dots span { width: 10px; height: 10px; border-radius: 50%; border: 1.5px solid var(--white); }
  .hero-dots .is-current { background: var(--white); }
  .intro-band {
    position: absolute;
    left: 110px; top: 430px;
    width: 966px; height: 212px;
    background: var(--band);
  }
  .welcome { position: absolute; left: 19px; top: 28px; width: 552px; color: var(--white); }
  .welcome h1 { font-size: 21px; font-weight: 700; margin-bottom: 9px; }
  .welcome p { font-size: 13.2px; line-height: 18.4px; }
  .btn-more {
    display: inline-block;
    margin-top: 17px;
    background: var(--soft-pink);
    color: var(--ink);
    font-size: 12.5px;
    padding: 4px 9px;
    text-decoration: none;
  }
  .hours-card {
    position: absolute;
    left: 640px; top: 29px;
    width: 307px; height: 159px;
    border-radius: 14px;
    overflow: hidden;
    background: linear-gradient(180deg, var(--grey-light), var(--grey-mid));
    border-top: 18px solid #e8619b;
    border-bottom: 16px solid #e8619b;
    padding: 10px 0 0 37px;
    color: var(--text-dark);
  }
  .hours-card h2 { font-size: 18px; font-weight: 700; margin-bottom: 11px; }
  .hours-card p { font-size: 13px; line-height: 26px; }
  .hours-card a { color: var(--hot-pink); text-decoration: none; font-size: 13px; }
  .services {
    position: absolute;
    left: 110px; top: 642px;
    width: 966px; height: 48px;
    background: #f6f6f6;
  }
  .services .divider { position: absolute; left: 19px; right: 19px; top: 5px; border-top: 3px dashed var(--hot-pink); }
  .services h2 {
    position: absolute; left: 0; right: 0; top: 20px;
    text-align: center;
    color: var(--hot-pink);
    font-size: 21px; font-weight: 700;
  }
</style>
</head>
<body>
  <nav class="main-nav">
    <a class="is-active" href="#" style="left:127px;">Home</a>
    <a href="#" style="left:227px;">About Us</a>
    <a href="#" style="left:346px;">Services</a>
    <a href="#" style="left:778px;">Gallery</a>
    <a href="#" style="left:892px;">Blog</a>
    <a href="#" style="left:980px;">Contacts</a>
  </nav>

  <div class="page-frame"></div>

  <div class="logo">
    <span class="logo-name">VELMORIN</span>
    <span class="logo-sub">Hair Studio</span>
  </div>

  <section class="hero" role="img" aria-label="Two fashion models with sculpted red curly and platinum blonde hairstyles against a turquoise backdrop">
    <div class="hero-headline"><span class="initial">L</span>eading <span class="initial">S</span>tylist at<br>fashion shows and<br>photo shoots</div>
    <svg class="hero-arrow prev" width="22" height="22" viewBox="0 0 22 22" aria-hidden="true">
      <circle cx="11" cy="11" r="9.5" fill="none" stroke="#fff" stroke-width="2"/>
      <path d="M12.5 7 L8.5 11 L12.5 15" fill="none" stroke="#fff" stroke-width="2"/>
    </svg>
    <svg class="hero-arrow next" width="22" height="22" viewBox="0 0 22 22" aria-hidden="true">
      <circle cx="11" cy="11" r="9.5" fill="none" stroke="#fff" stroke-width="2"/>
      <path d="M9.5 7 L13.5 11 L9.5 15" fill="none" stroke="#fff" stroke-width="2"/>
    </svg>
    <div class="hero-dots"><span></span><span class="is-current"></span><span></span></div>
  </section>

  <section class="intro-band">
    <div class="welcome">
      <h1>Welcome to VELMORIN Hair Studio!</h1>
      <p>Our salon is based on the belief that our customers needs are of the utmost importance. Our team is committed to meeting those needs. As a result, a high percentage of our business is from repeat customers and referrals. We would welcome the opportunity to earn your trust and deliver you the best service in the industry!</p>
      <a class="btn-more" href="#">More About Us</a>
    </div>
    <aside class="hours-card">
      <h2>Opening hours</h2>
      <p>Monday - Saturday: 10am - 10pm</p>
      <p>Sunday: 12pm - 6pm</p>
      <a href="#">Make an Appointment</a>
    </aside>
  </section>

  <section class="services">
    <div class="divider"></div>
    <h2>Our Hair Salon Services</h2>
  </section>
</body>
</html>
```